Business Card Design for Tidewell

The company provides engineering tender consulting services and personnel resources. The target market is large engineering construction and services companies. The business is based in Australia.

```html
<!DOCTYPE html>
<html lang="en">
<head>
<meta charset="utf-8">
<title>Tidewell Business Card</title>
<link rel="stylesheet" href="https://fonts.googleapis.com/css2?family=Oswald:wght@400&family=PT+Sans:wght@400;700&display=swap">
<style>
  :root {
    --page: #ffffff;
    --card: #e6e7e8;
    --ink: #231f20;
    --band: #231f20;
    --band-text: #ffffff;
  }
  * { margin: 0; padding: 0; box-sizing: border-box; }
  html, body {
    width: 1200px;
    height: 1000px;
    overflow: hidden;
    background: var(--page);
  }
  .canvas {
    position: relative;
    width: 1200px;
    height: 1000px;
    font-family: "PT Sans", sans-serif;
    color: var(--ink);
  }
  .card {
    position: absolute;
    top: 151px;
    width: 426px;
    height: 702px;
    background: var(--card);
  }
  .card--front { left: 144px; }
  .card--back { left: 637px; }

  .card__header {
    position: absolute;
    top: 0; left: 0;
    width: 100%;
    height: 96px;
    background: var(--band);
    display: flex;
    align-items: center;
    justify-content: center;
  }
  .brand-name {
    font-family: "Oswald", sans-serif;
    font-weight: 400;
    font-size: 56px;
    letter-spacing: 1px;
    color: var(--band-text);
    line-height: 1;
  }
  .slogan {
    position: absolute;
    top: 106px;
    right: 23px;
    font-size: 14px;
    letter-spacing: 0.5px;
    text-transform: uppercase;
    word-spacing: 2px;
    white-space: nowrap;
  }

  .holder {
    position: absolute;
    left: 17px;
    top: 453px;
  }
  .holder__name {
    font-size: 28px;
    line-height: 1.1;
  }
  .holder__position {
    font-size: 15px;
    margin-top: 8px;
  }
  .divider {
    position: absolute;
    left: 12px;
    top: 536px;
    width: 277px;
    height: 2px;
    background: var(--ink);
  }
  .contact {
    position: absolute;
    left: 13px;
    top: 559px;
    list-style: none;
    font-size: 17px;
    line-height: 23.5px;
    white-space: nowrap;
  }
  .card__foot-rule {
    position: absolute;
    left: 0; bottom: 0;
    width: 100%;
    height: 8px;
    background: var(--band);
  }

  .services {
    position: absolute;
    left: 64px;
    top: 240px;
    list-style: none;
    font-size: 17px;
    line-height: 30px;
    white-space: nowrap;
  }
  .services li::before {
    content: "-";
    font-weight: 700;
    display: inline-block;
    width: 16px;
  }
  .card__footer {
    position: absolute;
    left: 0; bottom: 0;
    width: 100%;
    height: 44px;
    background: var(--band);
    color: var(--band-text);
    font-size: 18px;
    display: flex;
    align-items: center;
    justify-content: center;
  }
</style>
</head>
<body>
<main class="canvas">
  <section class="card card--front">
    <header class="card__header"><span class="brand-name">Tidewell</span></header>
    <p class="slogan">Tenders &amp; Personnel</p>
    <div class="holder">
      <p class="holder__name">Jordan Marlowe</p>
      <p class="holder__position">Tender Consultant</p>
    </div>
    <div class="divider"></div>
    <ul class="contact">
      <li>Mobile : 0412&nbsp; 555&nbsp; 018</li>
      <li>Telephone : 07&nbsp; 5550&nbsp; 1234</li>
      <li>E-mail : hello@tidewell.com.au</li>
      <li>PO BOX 42 Southport, QLD, 4215</li>
      <li>ABN 51 824 753 556</li>
    </ul>
    <div class="card__foot-rule"></div>
  </section>

  <section class="card card--back">
    <header class="card__header"><span class="brand-name">Tidewell</span></header>
    <p class="slogan">Tenders &amp; Personnel</p>
    <ul class="services">
      <li>Tender strategy &amp; planning</li>
      <li>Bid writing &amp; management</li>
      <li>Pricing &amp; estimating support</li>
      <li>Compliance review</li>
      <li>Proposal design</li>
      <li>Engineering personnel supply</li>
      <li>Contract staffing</li>
      <li>Project recruitment</li>
      <li>Capability statements</li>
      <li>Post-tender debriefs</li>
    </ul>
    <footer class="card__footer">www.tidewell.com.au</footer>
  </section>
</main>
</body>
</html>
```